Derek Hollins Business card

Hey there, I’m hoping to have a business card designed. I’m in Real estate and just switched to a new Brokerage called: The Property Quarter

The back could just be the company name maybe or whatever looks good!

I’ve attached some logos of our company and some cards my buddy had done up.

On the card:
Derek Hollins
derekhollins@mailbox-demo.com
587-214-6093
derekhollins-demo.ca

Target Market(s)

Home buyers and sellers

Industry/Entity Type

Real Estate

Contact Information for Business Card

just looking for a cool and modern design with my picture on it. I like the idea of Black and red being used.

Requirements
Must have
• all the details provided. I'm open to anything. Just want a professional looking card.

```html
<!DOCTYPE html>
<html lang="en">
<head>
<meta charset="utf-8">
<title>Derek Hollins – Business Card</title>
<link rel="stylesheet" href="https://fonts.googleapis.com/css2?family=Montserrat:wght@700;800&family=Lato:wght@400&display=swap">
<style>
  :root {
    --backdrop: #3a3a3a;
    --card-black: #050505;
    --card-white: #ffffff;
    --brand-red: #cc1f39;
    --ink: #0a0a0c;
    --suit-navy: #2a3140;
    --photo-light: #e9ebee;
  }
  * { box-sizing: border-box; margin: 0; padding: 0; }
  html, body {
    width: 1200px; height: 694px; overflow: hidden;
    background: var(--backdrop);
  }
  .stage {
    position: relative; width: 1200px; height: 694px;
    display: flex; align-items: center; justify-content: center; gap: 40px;
  }
  .card {
    position: relative; width: 540px; height: 309px; overflow: hidden;
    box-shadow: 0 14px 30px rgba(0,0,0,.45);
  }

  /* Back side */
  .card-back {
    background: var(--card-black);
    display: flex; align-items: center; justify-content: center;
  }
  .card-back .brand-name {
    font-family: "Montserrat", sans-serif; font-weight: 800;
    font-size: 50px; line-height: 1; letter-spacing: -1px;
    color: var(--card-white); text-align: center;
  }

  /* Front side */
  .card-front { background: var(--card-white); }
  .card-front .brand-name {
    position: absolute; left: 34px; top: 52px; width: 320px;
    font-family: "Montserrat", sans-serif; font-weight: 800;
    font-size: 42px; line-height: 1.02; letter-spacing: -1px;
    color: var(--ink);
  }
  .portrait {
    position: absolute; right: 0; top: 0; width: 180px; height: 309px;
    background: linear-gradient(180deg, var(--photo-light) 0%, #8a909c 45%, var(--suit-navy) 100%);
  }
  .name-band {
    position: absolute; left: 0; top: 192px; width: 360px; height: 36px;
    background: var(--brand-red);
    display: flex; align-items: center; padding-left: 36px;
  }
  .agent-name {
    font-family: "Montserrat", sans-serif; font-weight: 800;
    font-size: 20px; color: var(--card-white);
  }
  .contact-panel {
    position: absolute; left: 0; top: 228px; width: 360px; height: 73px;
    background: var(--card-black);
    padding: 8px 0 0 40px;
  }
  .contact-list { list-style: none; }
  .contact-item {
    display: flex; align-items: center; gap: 10px; height: 20px;
    font-family: "Lato", sans-serif; font-size: 13px; color: var(--card-white);
  }
  .contact-item svg { width: 12px; height: 12px; flex: none; }
  .bottom-stripe {
    position: absolute; left: 0; bottom: 0; width: 100%; height: 8px;
    background: var(--brand-red);
  }
</style>
</head>
<body>
<main class="stage">
  <section class="card card-back" aria-label="Card back">
    <h1 class="brand-name">The Property<br>Quarter</h1>
  </section>

  <section class="card card-front" aria-label="Card front">
    <h2 class="brand-name">The Property Quarter</h2>
    <div class="portrait" role="img" aria-label="Portrait photo of Derek Hollins in a dark suit and white shirt"></div>
    <div class="name-band"><p class="agent-name">Derek Hollins</p></div>
    <div class="contact-panel">
      <ul class="contact-list">
        <li class="contact-item">
          <svg viewBox="0 0 12 12" aria-hidden="true"><path fill="#cc1f39" d="M2.5 0.8l1.8 2.3-1 1.2c.7 1.5 1.8 2.6 3.3 3.3l1.2-1 2.3 1.8-.9 1.9C5 9.8 2.2 7 1 1.7z"/></svg>
          587-214-6093
        </li>
        <li class="contact-item">
          <svg viewBox="0 0 12 12" aria-hidden="true"><rect x="0.5" y="2.5" width="11" height="7.5" fill="#cc1f39"/><path d="M0.8 2.8L6 7l5.2-4.2" fill="none" stroke="#050505" stroke-width="1"/></svg>
          derekhollins@mailbox-demo.com
        </li>
        <li class="contact-item">
          <svg viewBox="0 0 12 12" aria-hidden="true"><circle cx="6" cy="6" r="5.5" fill="#cc1f39"/><path d="M0.8 6h10.4M6 0.5c-2.2 2.9-2.2 8.1 0 11M6 0.5c2.2 2.9 2.2 8.1 0 11" fill="none" stroke="#050505" stroke-width="0.8"/></svg>
          derekhollins-demo.ca
        </li>
      </ul>
    </div>
    <div class="bottom-stripe"></div>
  </section>
</main>
</body>
</html>
```